Business Card Design

I am starting my therapy private practice. I will be an in home therapist, so I go into family's homes instead of using an office to do family/marriage therapy. Therefore, I do not have an office address. I am looking for something in the black, red, gray, and blue color scheme that appeals to both families, couples and teenagers.

Industry/Entity Type

Business

Contact Information for Business Card

Lena Brovick, MS, MFT Intern
Marriage and Family Therapy
In Home Therapist
508-241-6039
Lena@LenaBrovick.net

```html
<!DOCTYPE html>
<html lang="en">
<head>
<meta charset="utf-8">
<title>Lena Brovick – Business Card</title>
<link rel="stylesheet" href="https://fonts.googleapis.com/css2?family=Parisienne&family=Courgette&family=Tinos&family=Open+Sans:wght@400&display=swap">
<style>
  :root {
    --backdrop: #d4d4d4;
    --card-white: #ffffff;
    --frame-black: #0d0d0d;
    --ink: #111111;
    --accent-red: #c8161d;
    --accent-red-dark: #8f0d12;
    --ghost-gray: #ececec;
  }
  * { box-sizing: border-box; margin: 0; padding: 0; }
  html, body {
    width: 1200px; height: 900px; overflow: hidden;
    background: var(--backdrop);
  }
  .canvas {
    position: relative; width: 1200px; height: 900px;
    display: flex; align-items: center; justify-content: center;
  }
  .business-card {
    position: relative; width: 960px; height: 560px;
    background: var(--card-white);
    border-radius: 48px;
    padding: 14px;
    box-shadow: 0 10px 30px rgba(0,0,0,0.18);
  }
  .card-frame {
    position: relative; width: 100%; height: 100%;
    border: 13px solid var(--frame-black);
    border-radius: 38px;
    background: var(--card-white);
    overflow: hidden;
  }
  .family-emblem {
    position: absolute; left: 28px; top: 26px;
    width: 270px; height: 290px;
    border-radius: 48% 48% 12px 12px;
    background: radial-gradient(ellipse at 50% 35%, #e2272e 0%, var(--accent-red) 45%, var(--accent-red-dark) 100%);
  }
  .family-emblem-faint {
    position: absolute; right: -10px; top: 150px;
    width: 260px; height: 370px;
    border-radius: 48% 48% 12px 12px;
    background: linear-gradient(180deg, #f1f1f1 0%, var(--ghost-gray) 100%);
  }
  .identity {
    position: absolute; left: 285px; top: 78px;
    width: 400px; text-align: center;
  }
  .role-tagline {
    font-family: "Courgette", cursive;
    color: var(--accent-red);
    font-size: 21px;
    margin-left: -20px;
  }
  .therapist-name {
    font-family: "Parisienne", cursive;
    color: var(--ink);
    font-size: 72px; font-weight: 400;
    line-height: 1.1; margin-top: -2px;
    white-space: nowrap;
  }
  .credentials {
    font-family: "Tinos", serif;
    color: var(--accent-red);
    font-size: 17px; white-space: nowrap;
    margin-top: -2px;
  }
  .contact-list {
    position: absolute; left: 36px; bottom: 44px;
    list-style: none;
    font-family: "Open Sans", sans-serif;
    color: var(--ink); font-size: 28px; line-height: 1.25;
  }
  .contact-item { display: flex; align-items: center; gap: 10px; }
  .contact-icon { width: 26px; height: 26px; flex: none; }
</style>
</head>
<body>
<main class="canvas">
  <article class="business-card">
    <div class="card-frame">
      <div class="family-emblem-faint" role="img" aria-label="Faint family tree emblem decoration"></div>
      <div class="family-emblem" role="img" aria-label="Red family tree emblem with parents and child"></div>

      <header class="identity">
        <p class="role-tagline">In Home Therapist</p>
        <h1 class="therapist-name">Lena Brovick</h1>
        <p class="credentials">MS, MFT Intern Marriage and Family Therapy</p>
      </header>

      <ul class="contact-list">
        <li class="contact-item">
          <svg class="contact-icon" viewBox="0 0 24 24" aria-hidden="true">
            <path fill="#c8161d" d="M6.6 10.8c1.4 2.8 3.8 5.1 6.6 6.6l2.2-2.2c.3-.3.7-.4 1-.2 1.1.4 2.3.6 3.6.6.6 0 1 .4 1 1V20c0 .6-.4 1-1 1C10.6 21 3 13.4 3 4c0-.6.4-1 1-1h3.5c.6 0 1 .4 1 1 0 1.3.2 2.5.6 3.6.1.3 0 .7-.2 1z"/>
          </svg>
          <span>508-241-6039</span>
        </li>
        <li class="contact-item">
          <svg class="contact-icon" viewBox="0 0 24 24" aria-hidden="true">
            <rect x="2" y="5" width="20" height="14" rx="1.5" fill="#c8161d"/>
            <path d="M3 6.5l9 6.5 9-6.5" fill="none" stroke="#ffffff" stroke-width="1.6"/>
          </svg>
          <span>Lena@LenaBrovick.net</span>
        </li>
      </ul>
    </div>
  </article>
</main>
</body>
</html>
```